female inspired Gin Label

I have been asked to create a gin for a well know woman who lives in Liverpool and has her own brand of merchandise, beauty products and now wishes to have her own gin.
She goes by the name of 'Tindle Vane' which is Liverpool slang for a woman living in Liverpool.
I would like the gin to be 70cl and 40% vol.
With the writing 'Tindle Vane Gin' The style we want is either like a tattoo style and also as attached on the document... so illustrations of all things female, like hairdryer, nail varnish, gin and tonic, cocktails, lip stick hair brush etc.

```html
<!DOCTYPE html>
<html lang="en">
<head>
<meta charset="utf-8">
<title>Tindle Vane Gin – Label</title>
<link rel="stylesheet" href="https://fonts.googleapis.com/css2?family=Playfair+Display:wght@700&family=Josefin+Sans:wght@300;400&display=swap">
<style>
  :root {
    --backdrop: #e6e8ec;
    --label-cream: #ecdcb9;
    --frame-gold: #c9a25e;
    --dot-gold: #d3a86a;
    --title-rose: #c38d85;
    --ink: #1e1a17;
    --art-tone: #d9c6a2;
  }
  * { margin: 0; padding: 0; box-sizing: border-box; }
  html, body {
    width: 1138px;
    height: 1200px;
    overflow: hidden;
    background: var(--backdrop);
  }
  .canvas {
    position: relative;
    width: 1138px;
    height: 1200px;
  }
  .label {
    position: absolute;
    left: 196px;
    top: 100px;
    width: 746px;
    height: 1000px;
    background: var(--label-cream);
    border: 2px solid var(--frame-gold);
  }
  .label__rule {
    position: absolute;
    inset: 10px;
    border: 1px solid var(--frame-gold);
  }
  .label__dotted {
    position: absolute;
    inset: 28px;
    border: 3px dotted var(--dot-gold);
  }
  .label__art {
    position: absolute;
    left: 90px;
    top: 56px;
    width: 580px;
    height: 570px;
    border-radius: 46% 48% 40% 42% / 40% 44% 52% 50%;
    background: radial-gradient(ellipse at 50% 45%, var(--art-tone) 0%, rgba(217,198,162,0.55) 60%, rgba(236,220,185,0) 100%);
  }
  .label__title {
    position: absolute;
    left: 0;
    right: 0;
    top: 640px;
    text-align: center;
    font-family: "Playfair Display", serif;
    font-weight: 700;
    font-size: 112px;
    line-height: 1;
    letter-spacing: -3px;
    color: var(--title-rose);
  }
  .label__gin {
    position: absolute;
    left: 0;
    right: 0;
    top: 770px;
    text-align: center;
    font-family: "Josefin Sans", sans-serif;
    font-weight: 300;
    font-size: 104px;
    line-height: 1;
    color: var(--ink);
  }
  .label__tagline {
    position: absolute;
    left: 0;
    right: 0;
    top: 868px;
    text-align: center;
    font-family: "Josefin Sans", sans-serif;
    font-weight: 400;
    font-size: 20px;
    line-height: 1.05;
    color: var(--ink);
  }
  .label__volume,
  .label__abv {
    position: absolute;
    top: 924px;
    font-family: "Josefin Sans", sans-serif;
    font-weight: 400;
    font-size: 24px;
    color: var(--ink);
  }
  .label__volume { left: 88px; }
  .label__abv { right: 92px; }
</style>
</head>
<body>
  <main class="canvas">
    <section class="label">
      <div class="label__rule"></div>
      <div class="label__dotted"></div>
      <div class="label__art" role="img" aria-label="Tattoo-style line illustration cluster of feminine items: cocktail glass, roses, scissors, hairdryer, hand mirror, swallow, lipstick, nail varnish and a diamond"></div>
      <h1 class="label__title">Tindle Vane</h1>
      <p class="label__gin">GIN</p>
      <p class="label__tagline">THE SPIRIT OF<br>LIVERPOOL</p>
      <p class="label__volume">70 cl</p>
      <p class="label__abv">40% vol</p>
    </section>
  </main>
</body>
</html>
```